Briar Crest personal care products line

I need a label design for a line of shampoo, conditioner, beard oil, body butter, massage oil, all containing Hemp oil, All Natural product. No phosphates,
I want the design to feel unisex but want to keep it clean as possible. This is for upscale salons and needs to say on the label professional styling products on the label. Please visit my facebook page www.plumvale.net/briarcrest to see the description of the product benefits. I am attaching some ideas I like as well as the briar crest logo. I would like to see any color of bottle you best think will suit this product as well as new logo design. I am not set on any of these elements. Just the name Briar Crest.
Updates

Project Deadline Extended Reason: I have extended the deadline as I had not filled out the description for the design as it should be. I have also added some features that will define the idea as to what we need. I am open to any desing using Briar Crest. The tag line is not anything I am determined to keep either. Please just be creative and help come up with a great product label for this name and product.Thank you to all ! Added Tuesday, June 2, 2015

Target Market(s)

Salons and upper end market

Industry/Entity Type

Cosmetology

Font styles to use
Serif
Sans Serif

Requirements
Must have
• Logo
Nice to have
• Bottle and packaging ideas on color and shape of bottle

```html
<!DOCTYPE html>
<html lang="en">
<head>
<meta charset="utf-8">
<title>Briar Crest – Professional Styling Products Label</title>
<link rel="stylesheet" href="https://fonts.googleapis.com/css2?family=Alegreya:ital,wght@0,400;1,400&family=Arimo&display=swap">
<style>
  :root {
    --mustard: #d6be5a;
    --mustard-dark: #9e8738;
    --accent-violet: #9a2fd6;
    --label-outline: #000000;
    --label-ring: #6e5a7a;
    --label-face: #cca3dc;
    --label-band: #a886b8;
    --ink-green: #1e3320;
    --ink-tagline: #2f3d2a;
    --ink-url: #4a6b45;
    --mark-green: #6aa535;
  }
  html, body {
    margin: 0;
    padding: 0;
    width: 1200px;
    height: 900px;
    overflow: hidden;
    background: var(--mustard);
  }
  .label-canvas {
    display: block;
    width: 1200px;
    height: 900px;
  }
  .brand-name {
    font-family: "Alegreya", Georgia, serif;
    font-weight: 400;
    font-size: 84px;
    fill: var(--ink-green);
  }
  .tagline {
    font-family: "Alegreya", Georgia, serif;
    font-style: italic;
    font-size: 40px;
    fill: var(--ink-tagline);
  }
  .web-address {
    font-family: "Arimo", Arial, sans-serif;
    font-size: 27px;
    fill: var(--ink-url);
  }
  .product-line {
    font-family: "Alegreya", Georgia, serif;
    font-style: italic;
    font-size: 46px;
    fill: var(--ink-tagline);
  }
</style>
</head>
<body>
<svg class="label-canvas" viewBox="0 0 1200 900" xmlns="http://www.w3.org/2000/svg">
  <defs>
    <clipPath id="label-face-clip">
      <ellipse cx="590" cy="455" rx="496" ry="322"/>
    </clipPath>
  </defs>

  <!-- backdrop -->
  <rect class="backdrop" width="1200" height="900" fill="var(--mustard)"/>
  <polygon class="backdrop-band" points="995,0 1200,0 1200,310" fill="var(--mustard-dark)"/>
  <polygon class="backdrop-band" points="0,645 165,900 0,900" fill="var(--mustard-dark)"/>
  <rect class="top-rule" width="1200" height="4" fill="var(--accent-violet)"/>

  <!-- oval label -->
  <ellipse class="label-outline" cx="590" cy="455" rx="532" ry="358" fill="var(--label-outline)"/>
  <ellipse class="label-ring" cx="590" cy="455" rx="516" ry="342" fill="var(--label-ring)"/>
  <ellipse class="label-face" cx="590" cy="455" rx="496" ry="322" fill="var(--label-face)"/>
  <rect class="label-band" x="0" y="608" width="1200" height="300" fill="var(--label-band)" clip-path="url(#label-face-clip)"/>

  <!-- brand block -->
  <rect class="brand-frame" x="322" y="229" width="566" height="188" rx="6" fill="none" stroke="var(--ink-green)" stroke-width="6"/>
  <circle class="brand-dot" cx="345" cy="345" r="58" fill="var(--mark-green)"/>
  <text class="brand-name" x="625" y="370" text-anchor="middle">Briar Crest</text>

  <!-- tagline with rules -->
  <g class="tagline-rules" stroke="var(--ink-green)" stroke-width="1.5">
    <line x1="372" y1="441" x2="418" y2="441"/>
    <line x1="345" y1="466" x2="422" y2="466"/>
    <line x1="812" y1="441" x2="890" y2="441"/>
    <line x1="818" y1="466" x2="894" y2="466"/>
  </g>
  <text class="tagline" x="614" y="467" text-anchor="middle" textLength="346" lengthAdjust="spacing">Care that goes to the root</text>
  <text class="web-address" x="608" y="512" text-anchor="middle">www.briarcrestco.net</text>

  <!-- product line -->
  <text class="product-line" x="620" y="695" text-anchor="middle" transform="rotate(-2 620 685)">Professional styling products</text>
</svg>
</body>
</html>
```